Local Flower Farm Needs Business Card Design

I need business cards designed for a flower farm based in Eudora, Kansas.
Business Info:
We are a local cut flower farm located in Eudora, Kansas, founded by Darla Hoffstrom. What started as a passion for agriculture and search for more joy in daily life has blossomed into a small business dedicated to providing the community with beautiful, fresh, and sustainable flowers. We specialize in local, seasonal blooms, ensuring that every petal reflects the care and dedication we pour into our craft. Our mission is to deliver the highest quality flowers directly to our customers through local farmers markets and to florists who share our commitment to sustainability. Join us in celebrating the beauty of nature, one bloom at a time!
Contact Details:
Darla Hoffstrom
Owner
Phone 913-555-0147
Facebook: Lorabelle Quinn Blossoms
Instagram: @LorabelleQuinnBlossoms
Website: LorabelleQuinnBlossoms.example
Target Market(s)
Wholesale to Florists and Direct to Consumer via Farmers Market
Industry/Entity Type
Florist, Farm
Contact Information for Business Card
Name, Contact Info, Logo
Look and feel

```html
<!DOCTYPE html>
<html lang="en">
<head>
<meta charset="utf-8">
<title>Lorabelle Quinn Blossoms – Business Card</title>
<link rel="stylesheet" href="https://fonts.googleapis.com/css2?family=Tinos:wght@400;700&display=swap">
<style>
  :root {
    --backdrop: #c8c9ca;
    --card-white: #ffffff;
    --forest: #0d2a2d;
    --silver: #c3c5c7;
    --ink: #14302f;
    --on-dark: #ffffff;
  }
  * { margin: 0; padding: 0; box-sizing: border-box; }
  html, body {
    width: 1200px;
    height: 813px;
    overflow: hidden;
    background: var(--backdrop);
    font-family: "Tinos", "Times New Roman", serif;
  }
  .canvas {
    position: relative;
    width: 1200px;
    height: 813px;
    display: flex;
    align-items: center;
    justify-content: center;
    gap: 40px;
  }
  .card {
    position: relative;
    width: 540px;
    height: 310px;
    border-radius: 22px;
    background: var(--card-white);
    overflow: hidden;
    box-shadow: 0 6px 18px rgba(0,0,0,0.18);
  }
  .card-art {
    position: absolute;
    inset: 0;
    width: 100%;
    height: 100%;
  }

  /* Brand seal: circle with the business name set as plain text */
  .brand-seal {
    position: absolute;
    border: 1.5px solid var(--ink);
    border-radius: 50%;
    display: flex;
    align-items: center;
    justify-content: center;
    text-align: center;
    color: var(--ink);
    font-weight: 400;
    text-transform: uppercase;
  }
  .card--front .brand-seal {
    width: 210px;
    height: 210px;
    left: 165px;
    top: 50px;
    font-size: 23px;
    line-height: 1.25;
    letter-spacing: 2px;
  }
  .card--back .brand-seal {
    width: 112px;
    height: 112px;
    left: 28px;
    top: 52px;
    font-size: 12px;
    line-height: 1.25;
    letter-spacing: 1px;
  }

  .contact {
    position: absolute;
    right: 22px;
    text-align: right;
    color: var(--on-dark);
  }
  .contact-person { top: 118px; }
  .contact-name {
    font-weight: 700;
    font-size: 18px;
    letter-spacing: 0.2px;
  }
  .contact-role { font-size: 13px; margin-top: 2px; }
  .contact-list {
    top: 188px;
    list-style: none;
    font-size: 14px;
    line-height: 1.32;
  }
  .contact-list li {
    display: flex;
    justify-content: flex-end;
    align-items: center;
    gap: 6px;
  }
  .contact-icon {
    width: 11px;
    height: 11px;
    flex: none;
  }
</style>
</head>
<body>
<main class="canvas">

  <section class="card card--front" aria-label="Card front">
    <div class="brand-seal">Lorabelle<br>Quinn<br>Blossoms</div>
  </section>

  <section class="card card--back" aria-label="Card back">
    <svg class="card-art" viewBox="0 0 540 310" preserveAspectRatio="none" aria-hidden="true">
      <defs>
        <path id="wave" d="M0,262 C150,262 230,245 305,150 C370,65 440,34 560,28 L560,340 L0,340 Z"/>
      </defs>
      <use href="#wave" fill="var(--forest)" transform="translate(0,-34)"/>
      <use href="#wave" fill="var(--card-white)" transform="translate(0,-28)"/>
      <use href="#wave" fill="var(--silver)" transform="translate(0,-21)"/>
      <use href="#wave" fill="var(--card-white)" transform="translate(0,-10)"/>
      <use href="#wave" fill="var(--forest)"/>
    </svg>

    <div class="brand-seal">Lorabelle<br>Quinn<br>Blossoms</div>

    <div class="contact contact-person">
      <p class="contact-name">Darla Hoffstrom</p>
      <p class="contact-role">Owner</p>
    </div>

    <ul class="contact contact-list">
      <li>913-555-0147
        <svg class="contact-icon" viewBox="0 0 12 12" aria-hidden="true"><path fill="#fff" d="M2.5 1h2l1 2.5-1.3 1a6 6 0 0 0 3.3 3.3l1-1.3L11 7.5v2c0 .8-.7 1.5-1.5 1.5A8.5 8.5 0 0 1 1 2.5C1 1.7 1.7 1 2.5 1z"/></svg>
      </li>
      <li>LorabelleQuinnBlossoms.example
        <svg class="contact-icon" viewBox="0 0 12 12" aria-hidden="true"><circle cx="6" cy="6" r="5" fill="none" stroke="#fff" stroke-width="1.2"/><path d="M1 6h10M6 1c-2.5 3-2.5 7 0 10M6 1c2.5 3 2.5 7 0 10" fill="none" stroke="#fff" stroke-width="0.9"/></svg>
      </li>
      <li>Lorabelle Quinn Blossoms
        <svg class="contact-icon" viewBox="0 0 12 12" aria-hidden="true"><rect x="1" y="1" width="10" height="10" rx="2" fill="#fff"/></svg>
      </li>
      <li>@LorabelleQuinnBlossoms
        <svg class="contact-icon" viewBox="0 0 12 12" aria-hidden="true"><circle cx="6" cy="6" r="5" fill="#fff"/></svg>
      </li>
    </ul>
  </section>

</main>
</body>
</html>
```